Business Cards for a Junk Removal Company

Hello,
We are looking to have business cards designed that are simple, bold, easy to read, and right to the point. Please see the attachments for our logo files. We want the card to be yellow on both sides ( Color code Yellow: #FFE01B). The logo text font is (Rockstar Extra Bold) and this is also in the files attached. Please make the text black for the logo. On the back side of the card, you can use white and black for text. Thank you in advance for your hard work!

Front of card-
Harbor Haul Removal (logo)
Back of card-
Harbor Haul Removal
Donate - Recycle - Dispose
518-276-9053
www.harborhaulremoval.example
info@harborhaulremoval.example

Industry/Entity Type

Junk removal

Contact Information for Business Card

FRONT OF CARD- Harbor Haul Removal (logo) BACK OF CARD- Harbor Haul Removal Donate - Recycle - Dispose 518-276-9053 www.harborhaulremoval.example info@harborhaulremoval.example

Font styles to use
Other font styles liked:
• Rockstar Extra Bold

Colors
FFF300
FFF600
FEFA6F
FFFEC7
FFFEE8

Requirements
Must have
• Must have color code Yellow: #FFE01B for the background of front and back of the card

```html
<!DOCTYPE html>
<html lang="en">
<head>
<meta charset="utf-8">
<title>Harbor Haul Removal – Business Cards</title>
<link rel="stylesheet" href="https://fonts.googleapis.com/css2?family=Anton&display=swap">
<style>
  :root {
    --yellow: #f6d656;
    --ink: #231f20;
    --white: #ffffff;
    --stage: #4a4c50;
  }
  * { margin: 0; padding: 0; box-sizing: border-box; }
  html, body {
    width: 1200px; height: 887px; overflow: hidden;
    background: var(--stage);
    font-family: "Anton", "Impact", sans-serif;
  }
  .sheet {
    position: relative; width: 1200px; height: 887px;
    display: flex; flex-direction: column; align-items: center;
    justify-content: center; gap: 31px;
  }
  .card {
    position: relative; width: 700px; height: 400px;
    border-radius: 30px; overflow: hidden;
  }
  .card--front {
    background: var(--yellow);
    display: flex; align-items: center; justify-content: center;
  }
  .brand-name {
    text-transform: uppercase; letter-spacing: 2px; line-height: 0.95;
    text-align: center;
  }
  .card--front .brand-name { color: var(--white); font-size: 96px; }
  .card--back { background: var(--white); }
  .card__waves { position: absolute; inset: 0; width: 100%; height: 100%; }
  .card--back .brand-name {
    position: absolute; left: 52px; top: 44px;
    color: var(--yellow); font-size: 60px; text-align: left;
  }
  .tagline {
    position: absolute; right: 40px; top: 230px;
    color: var(--ink); text-transform: uppercase; text-align: right;
    font-size: 19px; letter-spacing: 1px; line-height: 1.45;
  }
  .contact-list {
    position: absolute; left: 92px; bottom: 26px; list-style: none;
    color: var(--ink); text-transform: uppercase;
    font-size: 18px; letter-spacing: 0.5px; line-height: 1.5;
  }
  .contact-list li { display: flex; align-items: center; gap: 10px; }
  .contact-list svg { width: 16px; height: 16px; fill: var(--ink); flex: none; }
</style>
</head>
<body>
<main class="sheet">
  <section class="card card--front" aria-label="Front of card">
    <h1 class="brand-name">Harbor Haul<br>Removal</h1>
  </section>

  <section class="card card--back" aria-label="Back of card">
    <svg class="card__waves" viewBox="0 0 700 400" preserveAspectRatio="none" aria-hidden="true">
      <path fill="var(--ink)" d="M0,300 C150,235 300,215 430,203 C560,190 650,150 700,55 L700,125 C650,188 560,215 430,224 C300,233 150,262 0,335 Z"/>
      <path fill="var(--yellow)" d="M0,345 C150,275 300,246 430,236 C560,224 650,192 700,140 L700,400 L0,400 Z"/>
    </svg>

    <h2 class="brand-name">Harbor Haul<br>Removal</h2>

    <p class="tagline">Harbor Haul Removal<br>Donate - Recycle - Dispose</p>

    <ul class="contact-list">
      <li>
        <svg viewBox="0 0 24 24" aria-hidden="true"><path d="M6.6 10.8a15.1 15.1 0 0 0 6.6 6.6l2.2-2.2a1 1 0 0 1 1-.25 11.4 11.4 0 0 0 3.6.57 1 1 0 0 1 1 1V20a1 1 0 0 1-1 1A17 17 0 0 1 3 4a1 1 0 0 1 1-1h3.5a1 1 0 0 1 1 1c0 1.25.2 2.45.57 3.6a1 1 0 0 1-.25 1z"/></svg>
        518-276-9053
      </li>
      <li>
        <svg viewBox="0 0 24 24" aria-hidden="true"><path d="M2 5h20v14H2z M4 7v.5l8 5 8-5V7l-8 5z" fill-rule="evenodd"/></svg>
        www.harborhaulremoval.example
      </li>
      <li>
        <svg viewBox="0 0 24 24" aria-hidden="true"><circle cx="12" cy="12" r="10"/><path d="M2 12h20M12 2c3 3 3 17 0 20M12 2c-3 3-3 17 0 20" stroke="var(--yellow)" stroke-width="1.5" fill="none"/></svg>
        info@harborhaulremoval.example
      </li>
    </ul>
  </section>
</main>
</body>
</html>
```